Flyer for Daycare

A Flyer for family group daycare
Specfs:
- One side english / Another Side spanish(the text for both sides is below)
- The flyer is for printing in 5" x 7" or 5.5" x 8.5"
- The address and phone number is the most important
Logo(see the attachment)
NYC Licensed
Children from 6 Weeks to 12 years old
Accepting All the Programs( TPB, OMW) and Private
CPR & First Aid Certified
Full Time, Part Time and After School
----------------------------------------------------------------------------
Provide Homework Assistance
Potty Training
Outdoor Activities
Nutritional Meals & Snack
Baby Wipes
Text in Spanish
Licencia por el estado de NY
Niños de 6 semanas a 12 años
Aceptando Todos los Programas (TPB, OMW) y Privado
Certificación en CPR y Primeros Auxilios
Tiempo completo, tiempo parcial y después de la escuela
----------------------------------------------------------------------------------------------
Actividades al aire libre
Asistencia con la tarea
Entrenamiento para ir al baño
Desayunos, Comidas y refrigerios nutricionales
Toallitas para bebé
582 E 416th ST
APT 4C
Bronx, NY, 10587
ig: @lumokidcare
555-718-2043
Target Market(s)
LAtin and Black, Bronx NY Area
Industry/Entity Type
Daycare service
Look and feel

```html
<!DOCTYPE html>
<html lang="en">
<head>
<meta charset="utf-8">
<title>Lumo Day Care Flyer</title>
<link href="https://fonts.googleapis.com/css2?family=Fredoka:wght@500;600;700&display=swap" rel="stylesheet">
<style>
  :root {
    --stage: #e9e9e9;
    --paper: #fbfbfb;
    --green: #1d7a0e;
    --navy: #1c2a8f;
    --red: #e10505;
    --red-side: #ee2f24;
    --orange: #f08a24;
    --teal: #0f8a8a;
    --mint: #5cc3a2;
    --yellow: #f1dc86;
    --wood: #d59b64;
    --wood-dark: #b97b45;
    --post: #4b2414;
    --logo: #2240a8;
  }
  * { margin: 0; padding: 0; box-sizing: border-box; }
  html, body { width: 1122px; height: 1200px; overflow: hidden; }
  body {
    background: var(--stage);
    font-family: "Fredoka", sans-serif;
    position: relative;
  }
  .flyer {
    position: absolute;
    left: 185px; top: 20px;
    width: 751px; height: 1160px;
    background: var(--paper);
    overflow: hidden;
    box-shadow: 0 6px 22px rgba(0,0,0,.18);
  }
  .hero-photo {
    position: absolute; left: 0; top: 0; width: 751px; height: 380px;
    background: linear-gradient(120deg, #d9c9b4 0%, #eee7de 35%, #f4f1ec 60%, #cfd9e4 100%);
  }
  .shapes { position: absolute; inset: 0; }
  .brand {
    position: absolute; left: 20px; top: 330px; width: 280px;
    display: flex; align-items: center; gap: 10px;
    font-weight: 700; font-size: 38px; line-height: 1.05; color: var(--logo);
  }
  .brand-dot { width: 26px; height: 26px; border-radius: 50%; background: var(--orange); flex: none; }
  .headline {
    position: absolute; left: 295px; top: 405px; width: 430px;
    text-align: center; color: var(--green);
    font-weight: 600; font-size: 34px; line-height: 45px;
  }
  .facts {
    position: absolute; left: 0; top: 528px; width: 751px;
    list-style: none; text-align: center; color: var(--navy);
    font-weight: 600; font-size: 23px; line-height: 35.7px;
  }
  .service {
    position: absolute; width: 150px; height: 160px;
    display: flex; align-items: center; justify-content: center; text-align: center;
    background: var(--red); color: #fff;
    border-radius: 48% 52% 45% 55% / 50% 44% 56% 50%;
    box-shadow: 4px 3px 0 -1px #fff, 6px 5px 0 0 var(--red);
    font-weight: 600; font-size: 20px; line-height: 29px;
  }
  .sign {
    position: absolute; background: var(--wood); color: #241208;
    text-align: center; font-weight: 600;
    box-shadow: inset 0 -6px 0 var(--wood-dark);
  }
  .sign-address { left: 216px; top: 1003px; width: 255px; height: 114px; transform: rotate(-4deg);
    font-size: 24px; line-height: 30px; padding-top: 12px; }
  .sign-contact { left: 510px; top: 997px; width: 218px; height: 100px; transform: rotate(5deg);
    font-size: 19px; line-height: 30px; padding: 16px 0 0 14px; text-align: left; }
  .contact-row { display: flex; align-items: center; gap: 7px; }
  .social-dot { width: 17px; height: 17px; border-radius: 50%; background: #241208; flex: none; }
  .flowers {
    position: absolute; left: 30px; top: 1050px; width: 230px; height: 110px;
    background: radial-gradient(ellipse at 30% 60%, #f2a07f 0%, #f6c98a 35%, rgba(251,251,251,0) 70%);
  }
</style>
</head>
<body>
  <main class="flyer">
    <div class="hero-photo" role="img" aria-label="Photo of two toddlers playing with stacking toys in a bright playroom"></div>

    <svg class="shapes" width="751" height="1160" viewBox="0 0 751 1160" aria-hidden="true">
      <path d="M0 300 C60 270 140 255 230 275 C330 300 420 345 560 350 C650 352 720 330 751 300 L751 1160 L0 1160 Z" fill="var(--paper)"/>
      <path d="M0 310 C60 280 130 268 200 275" fill="none" stroke="var(--orange)" stroke-width="9" stroke-linecap="round"/>
      <path d="M520 355 C590 335 650 335 700 355" fill="none" stroke="var(--teal)" stroke-width="5" stroke-linecap="round"/>
      <ellipse cx="-5" cy="545" rx="43" ry="135" fill="var(--red-side)"/>
      <ellipse cx="765" cy="530" rx="55" ry="175" fill="var(--orange)"/>
      <circle cx="700" cy="576" r="24" fill="var(--yellow)"/>
      <ellipse cx="-5" cy="925" rx="44" ry="110" fill="var(--teal)"/>
      <ellipse cx="765" cy="880" rx="40" ry="135" fill="var(--mint)"/>
      <circle cx="735" cy="1130" r="52" fill="var(--yellow)"/>
      <rect x="340" y="962" width="14" height="198" fill="var(--post)"/>
      <rect x="604" y="972" width="14" height="188" fill="var(--post)"/>
    </svg>

    <div class="brand"><span class="brand-dot"></span><span>Lumo Day Care</span></div>

    <h1 class="headline">Where Your Little Angel Can Grow and Learn</h1>

    <ul class="facts">
      <li>NYC Licensed</li>
      <li>Children from 6 Weeks to 12 years old</li>
      <li>Accepting All the Programs( TPB, OMW) and Private</li>
      <li>CPR &amp; First Aid Certified</li>
      <li>Full Time, Part Time and After School</li>
    </ul>

    <div class="service" style="left:37px;top:722px;">Provide<br>Homework<br>Assistance</div>
    <div class="service" style="left:165px;top:808px;">Potty<br>Training</div>
    <div class="service" style="left:304px;top:733px;">Outdoor<br>Activities</div>
    <div class="service" style="left:445px;top:814px;">Baby<br>Wipes</div>
    <div class="service" style="left:574px;top:719px;">Nutritional<br>Meals &amp;<br>Snack</div>

    <div class="flowers" role="img" aria-label="Illustration of colourful flowers"></div>

    <div class="sign sign-address">582 E 416th ST<br>APT 4C<br>Bronx, NY, 10587</div>
    <div class="sign sign-contact">
      <div class="contact-row"><span class="social-dot"></span>@lumokidcare</div>
      <div class="contact-row">
        <svg width="17" height="17" viewBox="0 0 24 24" aria-hidden="true"><path fill="#241208" d="M6.6 10.8a15.1 15.1 0 0 0 6.6 6.6l2.2-2.2c.3-.3.7-.4 1-.2 1.1.4 2.3.6 3.6.6.6 0 1 .4 1 1V20c0 .6-.4 1-1 1A17 17 0 0 1 3 4c0-.6.4-1 1-1h3.5c.6 0 1 .4 1 1 0 1.3.2 2.5.6 3.6.1.3 0 .7-.2 1z"/></svg>
        555-718-2043
      </div>
    </div>
  </main>
</body>
</html>
```